Plakat-Design für mobile Energiespeicher
Zielgruppe
Wir vertreiben mobile Energiespeicher und benötigen für unser Produkt einen Eyecatcher, der auf das Produkt aufmerksam macht. Unsere Zielgruppe sind erwachsene Personen.
Aufgabenstellung
Das Plakat ist für einen Kundenstopper bestimmt und sollte DIN-A0/DIN-A1-Größe haben. Wichtig ist, dass es ein Eyecatcher ist. Es kann sich um ein modernes Design handeln. Vielleicht ein knackiger Slogan? Auf dem Plakat selbst sollten nur wenige technische Details stehen. Dafür wird es separates Info-Material geben.

```html
<!DOCTYPE html>
<html lang="de">
<head>
<meta charset="utf-8">
<title>Voltnest – Kein Strom? Kein Problem</title>
<link rel="stylesheet" href="https://fonts.googleapis.com/css2?family=Big+Shoulders+Display:wght@700&display=swap">
<style>
  :root {
    --bg: #000000;
    --neon-stroke: #eef7b8;
    --neon-glow: #b6e04a;
    --brand-green: #a9d23c;
    --device-dark: #2e3033;
    --device-mid: #45484c;
    --device-accent: #8fd42a;
  }
  html, body {
    margin: 0;
    padding: 0;
    background: var(--bg);
    overflow: hidden;
  }
  .poster {
    position: relative;
    width: 881px;
    height: 1200px;
    background: var(--bg);
    overflow: hidden;
    font-family: "Big Shoulders Display", "Arial Narrow", sans-serif;
  }
  .headline {
    position: absolute;
    left: 0;
    top: 0;
    width: 881px;
    height: 420px;
    filter: drop-shadow(0 0 6px var(--neon-glow)) drop-shadow(0 0 14px rgba(182, 224, 74, 0.55));
  }
  .headline__line {
    font-family: "Big Shoulders Display", "Arial Narrow", sans-serif;
    font-weight: 700;
    fill: none;
    stroke: var(--neon-stroke);
    stroke-width: 2.4;
  }
  .product-visual {
    position: absolute;
    left: 157px;
    top: 549px;
    width: 592px;
    height: 420px;
    border-radius: 34px;
    background:
      linear-gradient(90deg, var(--device-dark) 0%, var(--device-mid) 55%, var(--device-dark) 84%, var(--device-accent) 86%, #6fb51c 100%);
    box-shadow: 0 0 40px rgba(143, 212, 42, 0.35), 0 0 90px rgba(143, 212, 42, 0.18);
  }
  .brand {
    position: absolute;
    left: 0;
    width: 881px;
    top: 1080px;
    text-align: center;
    font-family: "Big Shoulders Display", "Arial Narrow", sans-serif;
    font-weight: 700;
    font-size: 50px;
    letter-spacing: 6px;
    line-height: 1;
    color: var(--brand-green);
    text-transform: uppercase;
  }
</style>
</head>
<body>
  <main class="poster">
    <svg class="headline" viewBox="0 0 881 420" width="881" height="420" aria-label="Kein Strom? Kein Problem">
      <text class="headline__line" x="186" y="199" font-size="178" textLength="534" lengthAdjust="spacingAndGlyphs">KEIN STROM?</text>
      <text class="headline__line" x="165" y="378" font-size="178" textLength="578" lengthAdjust="spacingAndGlyphs">KEIN PROBLEM</text>
    </svg>

    <div class="product-visual" role="img" aria-label="Produktfoto: mobiler Energiespeicher in Dunkelgrau mit grüner Seitenblende, Display und vier Steckdosen"></div>

    <div class="brand">Voltnest</div>
  </main>
</body>
</html>
```